Create Oceanfront SEO Website – Cormant Haven

I am web developer to build a high-quality, SEO-optimized website. The site is fully structured with content, layout, and purpose clearly defined, and comes with keyword-rich SEO guidance to maximize search engine visibility. Domain names and page content are provided.

Developer Role:
Build a responsive, fast-loading website in WordPress, allowing us to edit and update content in the future.
Implement SEO best practices, including meta tags, structured data, and optimized content.
Ensure smooth navigation, intuitive UX, and visually appealing design.
Establish the website to a fully functional state, after which we will handle ongoing updates and changes.
Domain and website will be hosted by hostivel under my profile.
Key Highlights:
Structured website with ready-to-use content.
SEO-focused pages for maximum visibility.
Domains and site structure already defined.
Creative freedom in design within the provided framework.

Target Market(s)

vacationers

Industry/Entity Type

vacation and travel

Coding

Coded - Design and coding required

Colors
0054AA
0677BA
7BADD7
CADEEF
E8F1F8
0094D4
00A9DD
6FCCEA
C7EBF8
E9F6FB
00AB8E
00BBA5
67D7C9
C6EFE9
E9F9F6
FFF300
FFF600
FEFA6F
FFFEC7
FFFEE8

Requirements
Must have
• see brief

```html
<!DOCTYPE html>
<html lang="en">
<head>
<meta charset="utf-8">
<title>Cormant Haven Oceanfront Condo</title>
<link href="https://fonts.googleapis.com/css2?family=Arvo:wght@700&family=Great+Vibes&family=Poppins:wght@400;500;600;700&display=swap" rel="stylesheet">
<style>
:root{
  --blue:#0054AA;
  --blue-mid:#0677BA;
  --blue-soft:#7BADD7;
  --blue-pale:#CADEEF;
  --blue-mist:#E8F1F8;
  --cyan:#00A9DD;
  --cyan-bright:#00BFF0;
  --cyan-soft:#6FCCEA;
  --teal:#00AB8E;
  --teal-deep:#0c7c8a;
  --yellow:#FFF300;
  --ink:#1d2433;
  --night:#1a2434;
  --white:#ffffff;
  --sans:'Poppins',sans-serif;
  --slab:'Arvo',serif;
  --script:'Great Vibes',cursive;
}
*{box-sizing:border-box;margin:0;padding:0}
html,body{width:1200px;height:5017px;overflow:hidden}
body{position:relative;font-family:var(--sans);color:var(--ink);background:var(--white)}
.abs{position:absolute}
.script{font-family:var(--script);font-size:26px;color:var(--ink);line-height:1}
.section-title{font-family:var(--sans);font-weight:600;color:var(--blue);font-size:31px;line-height:1.1}
.center{text-align:center;left:0;width:1200px}
.underline{position:absolute;left:570px;width:60px;height:3px;border-radius:2px;background:var(--ink)}
.btn{position:absolute;display:flex;align-items:center;justify-content:center;font-size:11px;border-radius:3px;font-family:var(--sans);white-space:nowrap}
.btn-blue{background:var(--blue);color:var(--white)}
.btn-white{background:var(--white);color:var(--ink)}
.btn b{font-weight:700;margin-left:3px}
.palm{position:absolute;border-radius:50%;background:radial-gradient(circle at 40% 40%,#3f9a3a 0%,#2f7d2c 45%,rgba(47,125,44,0) 70%);opacity:.5}
.band-blue{position:absolute;left:0;width:1200px;background:linear-gradient(90deg,var(--blue) 0%,var(--teal-deep) 100%)}

/* hero */
.hero{position:absolute;top:0;left:0;width:1200px;height:600px;overflow:hidden}
.hero-photo{position:absolute;inset:0;background:linear-gradient(180deg,#10304f 0%,#1e5a7a 30%,#2a7f8f 50%,#5e6b55 72%,#3c3a2c 100%)}
.hero-shade{position:absolute;inset:0;background:linear-gradient(180deg,rgba(0,0,0,.35) 0%,rgba(0,0,0,.1) 40%,rgba(0,0,0,.25) 100%)}
.hero-band{position:absolute;left:0;top:560px;width:1200px;height:80px;background:linear-gradient(90deg,var(--blue-mid) 0%,var(--cyan) 60%,var(--cyan-bright) 100%)}
.logo{position:absolute;left:158px;top:16px;display:flex;align-items:center;gap:8px;color:var(--white)}
.logo-dot{width:44px;height:44px;border-radius:50%;background:var(--cyan)}
.logo-name{font-weight:700;font-size:16px;line-height:1.15}
.nav{position:absolute;left:522px;top:29px;display:flex;gap:24px;font-size:12px;color:var(--white)}
.nav .active{color:var(--cyan-bright);text-decoration:underline}
.hero-title{font-family:var(--slab);font-size:40px;color:var(--cyan-bright);line-height:44px;top:176px}
.hero-sub{top:268px;color:var(--white);font-size:17px;line-height:26px}
.hero-sub em{font-family:var(--script);font-style:normal;font-weight:400;font-size:22px}

/* amenities */
.amenity{position:absolute;display:flex;align-items:center;gap:12px;font-size:11px;font-weight:500;line-height:1.25;width:260px}
.amenity-icon{width:36px;height:36px;border-radius:50%;background:var(--blue-pale);border:2px solid var(--blue);flex:none}

/* explore */
.explore{position:absolute;top:1180px;left:0;width:1200px;height:500px}
.explore-bg{position:absolute;inset:0;background:var(--blue-mist)}
.explore-photo{position:absolute;right:0;top:0;width:620px;height:500px;background:linear-gradient(90deg,rgba(232,241,248,1) 0%,rgba(215,196,160,.6) 25%,#c9b38a 45%,#8aa08a 65%,#3b7ca0 100%)}
.body-text{font-size:11px;line-height:18px;color:var(--ink)}

/* welcome */
.photo{position:absolute;border-radius:20px;border:4px solid var(--white);box-shadow:0 6px 18px rgba(0,0,0,.15)}

/* testimonials */
.quote{position:absolute;left:405px;top:2550px;width:540px;font-size:17px;line-height:27.5px;color:var(--white)}
.arrow{position:absolute;color:var(--white);font-size:26px}

/* gallery */
.gallery-main{position:absolute;left:200px;top:3031px;width:800px;height:397px;border-radius:12px;background:linear-gradient(180deg,#5ea0bc 0%,#8fb6b0 20%,#b9a98a 45%,#9d8f7a 70%,#5f7a5a 100%)}
.thumb{position:absolute;top:3444px;width:82px;height:58px;border-radius:4px}

/* links band */
.guide{position:absolute;width:220px;text-align:center;color:var(--white);font-weight:600;font-size:15px;line-height:19px}
.guide-icon{width:72px;height:72px;border-radius:50%;background:var(--white);margin:0 auto 14px;display:flex;align-items:center;justify-content:center}

/* faq */
.faq{position:absolute;left:335px;width:530px;border:1px solid #e3e8ef;border-radius:4px;background:var(--white);box-shadow:0 2px 6px rgba(0,0,0,.05);font-size:10.5px;font-weight:600;padding:0 14px}
.faq .toggle{position:absolute;right:12px;top:50%;margin-top:-7px;width:14px;height:14px;border-radius:50%;background:#d7dce3}
.faq.open .toggle{background:var(--blue-mid)}

/* footer */
.footer-band{position:absolute;left:0;top:4520px;width:1200px;height:50px;background:linear-gradient(90deg,var(--cyan-soft) 0%,var(--cyan) 40%,var(--blue-mid) 100%)}
.footer-body{position:absolute;left:0;top:4570px;width:1200px;height:417px;background:linear-gradient(180deg,#26344a 0%,#141c28 100%)}
.footer-h{font-size:12px;font-weight:600;color:var(--cyan);letter-spacing:.3px}
.footer-list{font-size:11px;color:var(--white);line-height:25px}
.footer-links{font-size:10.5px;color:var(--white);line-height:18px}
.field{position:absolute;left:793px;width:251px;background:#eef0f3;border-radius:2px;font-size:9px;color:#9aa2ad;padding:7px 8px}
.bottom-bar{position:absolute;left:0;top:4987px;width:1200px;height:30px;background:var(--blue);color:var(--white);font-size:10px}
.social{position:absolute;top:8px;width:14px;height:14px;border-radius:50%;background:var(--white)}
</style>
</head>
<body>

<!-- HERO -->
<header class="hero">
  <div class="hero-photo" role="img" aria-label="Oceanfront view with palm trees and beach at dusk"></div>
  <div class="hero-shade"></div>
  <div class="logo"><span class="logo-dot"></span><span class="logo-name">Cormant Haven<br>Oceanfront Condo</span></div>
  <nav class="nav"><span class="active">Home</span><span>Local Area</span><span>Reviews</span><span>Blogs</span><span>Contact Us</span></nav>
  <span class="btn btn-white" style="left:931px;top:21px;width:113px;height:32px;font-weight:600">Quick Inquiry</span>
  <h1 class="abs center hero-title">Stay In Our Cormant Haven<br>Oceanfront Condo</h1>
  <p class="abs center hero-sub">Your Perfect <em>Flagler Beach</em> Getaway – <em>Ocean Views,</em><br><em>Modern Amenities,</em> And <em>Steps From The Sand.</em></p>
  <span class="btn btn-white" style="left:376px;top:341px;width:125px;height:30px">Book on <b>StayNest</b></span>
  <span class="btn btn-white" style="left:508px;top:341px;width:119px;height:30px">Book on <b>RentHarbor</b></span>
  <span class="btn btn-white" style="left:635px;top:341px;width:186px;height:30px">Book on <b>LeaseLocal</b></span>
</header>
<div class="hero-band" role="img" aria-label="Ocean wave decoration"></div>

<!-- AMENITIES -->
<div class="palm" role="img" aria-label="Palm leaf decoration" style="left:-60px;top:690px;width:220px;height:220px"></div>
<div class="palm" role="img" aria-label="Palm leaf decoration" style="right:-40px;top:940px;width:180px;height:200px"></div>
<p class="abs center script" style="top:744px">Featured Amenities</p>
<h2 class="abs center section-title" style="top:770px">Why Our Condo Is<br>Perfect For Your Stay</h2>
<span class="underline" style="top:846px"></span>

<div class="amenity" style="left:232px;top:888px"><span class="amenity-icon"></span>Oceanfront Balcony With<br>Panoramic Atlantic Views</div>
<div class="amenity" style="left:506px;top:888px"><span class="amenity-icon"></span>Steps From Flagler<br>Beach Shoreline</div>
<div class="amenity" style="left:768px;top:888px"><span class="amenity-icon"></span>Spacious Living Area,<br>Bedrooms, And Bathrooms</div>
<div class="amenity" style="left:232px;top:956px"><span class="amenity-icon"></span>Pet-Friendly<br>Accommodations For Dogs</div>
<div class="amenity" style="left:506px;top:956px"><span class="amenity-icon"></span>Fully Furnished Kitchen And<br>Modern Appliances</div>
<div class="amenity" style="left:768px;top:956px"><span class="amenity-icon"></span>Free Parking And Easy Access To<br>Local Shops And Restaurants</div>

<span class="btn btn-blue" style="left:392px;top:1033px;width:127px;height:30px">Book on <b>StayNest</b></span>
<span class="btn btn-blue" style="left:532px;top:1033px;width:115px;height:30px">Book on <b>RentHarbor</b></span>
<span class="btn btn-blue" style="left:664px;top:1033px;width:184px;height:30px">Book on <b>LeaseLocal</b></span>

<!-- EXPLORE -->
<section class="explore">
  <div class="explore-bg"></div>
  <div class="explore-photo" role="img" aria-label="Aerial view of the beach shoreline with oceanfront homes"></div>
</section>
<p class="abs script" style="left:156px;top:1272px">Explore</p>
<h2 class="abs section-title" style="left:156px;top:1298px;font-size:32px">Flagler Beach,<br>Florida</h2>
<span class="underline" style="left:156px;top:1370px"></span>
<p class="abs body-text" style="left:156px;top:1394px;width:385px">Flagler Beach Is A Charming Seaside Town On Florida's Atlantic Coast. Known For Its Historic Fishing Pier, Scenic A1A Highway, Family-Friendly Beaches, And Local Eateries, It's A Peaceful Alternative To Crowded Tourist Destinations. Visitors Love Strolling The Pier, Enjoying Fresh Seafood, And Exploring Nearby Parks And Nature Trails.</p>
<span class="btn btn-blue" style="left:158px;top:1504px;width:95px;height:30px">Book Now</span>

<!-- WELCOME -->
<div class="palm" role="img" aria-label="Palm leaf decoration" style="left:-50px;top:1710px;width:230px;height:230px"></div>
<div class="palm" role="img" aria-label="Palm leaf decoration" style="right:-40px;top:2090px;width:170px;height:200px"></div>
<div class="photo" role="img" aria-label="Bright condo bedroom with ocean-view windows" style="left:306px;top:1813px;width:332px;height:230px;background:linear-gradient(135deg,#e8e4dc 0%,#cfc6b5 40%,#9fc1d6 70%,#6fa2c0 100%)"></div>
<div class="photo" role="img" aria-label="Oceanfront condo building at twilight" style="left:206px;top:1989px;width:240px;height:160px;background:linear-gradient(180deg,#28477a 0%,#3e5f94 45%,#2a2f3c 75%,#1b1f28 100%)"></div>
<div class="abs" role="img" aria-label="Small beach emblem" style="left:510px;top:2065px;width:60px;height:52px;border-radius:50%;background:radial-gradient(circle,#6FCCEA 0%,#C7EBF8 70%,rgba(255,255,255,0) 72%)"></div>
<p class="abs script" style="left:701px;top:1830px">Welcome To</p>
<h2 class="abs section-title" style="left:701px;top:1855px">Your Flagler Beach<br>Vacation Home</h2>
<span class="underline" style="left:701px;top:1928px"></span>
<p class="abs body-text" style="left:701px;top:1952px;width:395px">Welcome To Your Coastal Retreat, Perfectly Situated Just Steps From The Beach. This Pet-Friendly Property Offers Stunning Ocean Views And The Convenience Of A Short Walk To The Shoreline, Making It Ideal For Both Relaxation And Adventure.</p>
<p class="abs body-text" style="left:701px;top:2039px;width:395px">Whether You're Unwinding On The Balcony Or Strolling With Your Pup Along The Sand, This Getaway Blends Comfort With An Unbeatable Location.</p>
<span class="btn btn-blue" style="left:700px;top:2104px;width:96px;height:30px">Book Now</span>

<div class="abs" role="img" aria-label="Three colourful surfboards standing in the sand" style="left:536px;top:2198px;width:136px;height:122px;border-radius:40px 40px 6px 6px;background:linear-gradient(90deg,#8b8fd6 0%,#f08a2c 50%,#67D7C9 100%);opacity:.85"></div>

<!-- TESTIMONIALS -->
<div class="band-blue" style="top:2320px;height:540px"></div>
<p class="abs center script" style="top:2402px;color:var(--white)">Testimonials</p>
<h2 class="abs center section-title" style="top:2428px;color:var(--cyan)">Our Clients Say</h2>
<span class="underline" style="top:2473px;background:var(--white)"></span>
<p class="abs" style="left:405px;top:2518px;font-size:10px;color:var(--cyan-soft)"><span style="color:var(--yellow);font-size:13px;letter-spacing:1px">★★★★★</span>&nbsp; July 2025 • Stayed With Kids</p>
<div class="abs" style="left:275px;top:2556px;width:100px;height:100px;border-radius:50%;background:var(--white);display:flex;align-items:center;justify-content:center">
  <svg width="44" height="36" viewBox="0 0 44 36"><path d="M0 36 V18 C0 8 6 2 16 0 L18 6 C12 8 10 12 10 16 H20 V36 Z M24 36 V18 C24 8 30 2 40 0 L42 6 C36 8 34 12 34 16 H44 V36 Z" fill="var(--blue-mid)"/></svg>
</div>
<p class="quote">Dana's Apt Was In A Perfect Location. Had Everything You Needed Inside As Well. We Had A Problem Finding The Unit When Checking In Since The Door Wasn't Labeled Like It Was Supposed To Be....</p>
<div class="abs" role="img" aria-label="Guest avatar" style="left:406px;top:2680px;width:40px;height:40px;border-radius:50%;background:linear-gradient(135deg,#CADEEF,#7BADD7)"></div>
<p class="abs" style="left:456px;top:2684px;font-size:11px;font-weight:600;color:var(--white);line-height:16px">Marla<br><span style="font-weight:400;font-size:9.5px;color:var(--blue-pale)">Atlanta, Georgia</span></p>
<span class="arrow" style="left:172px;top:2588px">‹</span>
<span class="arrow" style="left:1014px;top:2588px">›</span>

<!-- GALLERY -->
<div class="palm" role="img" aria-label="Palm leaf decoration" style="left:-50px;top:2880px;width:220px;height:230px"></div>
<div class="palm" role="img" aria-label="Palm leaf decoration" style="right:-40px;top:3420px;width:180px;height:200px"></div>
<p class="abs center script" style="top:2922px">Testimonials</p>
<h2 class="abs center section-title" style="top:2948px">Our Gallery</h2>
<span class="underline" style="top:2993px"></span>
<div class="gallery-main" role="img" aria-label="Aerial view of the condo building near the ocean"></div>
<span class="abs" style="left:246px;top:3454px;color:var(--blue-mid);font-size:22px">‹</span>
<span class="abs" style="left:944px;top:3454px;color:var(--blue-mid);font-size:22px">›</span>
<div class="thumb" role="img" aria-label="Condo entrance" style="left:273px;background:linear-gradient(135deg,#c8a46a,#5e8fb8)"></div>
<div class="thumb" role="img" aria-label="Aerial neighbourhood" style="left:368px;background:linear-gradient(135deg,#8fb6b0,#b9a98a)"></div>
<div class="thumb" role="img" aria-label="Pool deck" style="left:463px;background:linear-gradient(135deg,#3b6f8f,#6fb2c8)"></div>
<div class="thumb" role="img" aria-label="Beach walkway" style="left:558px;background:linear-gradient(135deg,#2f3a52,#9aa8bf)"></div>
<div class="thumb" role="img" aria-label="Ocean waves" style="left:653px;background:linear-gradient(135deg,#6FCCEA,#e9f6fb)"></div>
<div class="thumb" role="img" aria-label="Sunset over the water" style="left:748px;background:linear-gradient(180deg,#f2a24a,#3a3a4a)"></div>
<div class="thumb" role="img" aria-label="Condo doorway" style="left:843px;background:linear-gradient(135deg,#c8a46a,#4f7fa8)"></div>
<span class="btn btn-blue" style="left:580px;top:3536px;width:84px;height:30px">View All</span>

<!-- GUIDES BAND -->
<div class="band-blue" style="top:3680px;height:330px"></div>
<div class="guide" style="left:204px;top:3759px"><div class="guide-icon"><svg width="30" height="34" viewBox="0 0 30 34"><rect x="3" y="3" width="24" height="29" rx="3" fill="none" stroke="var(--blue)" stroke-width="2.5"/><path d="M9 12 H21 M9 18 H21 M9 24 H17" stroke="var(--blue)" stroke-width="2.5"/></svg></div>Plan your trip with our<br>Cormant Haven Travel<br>Guide</div>
<div class="guide" style="left:490px;top:3759px"><div class="guide-icon"><svg width="34" height="30" viewBox="0 0 34 30"><path d="M3 22 H31 M6 22 C6 12 28 12 28 22" fill="none" stroke="var(--blue)" stroke-width="2.5"/><circle cx="17" cy="9" r="2.5" fill="var(--blue)"/></svg></div>Discover the best<br>restaurants in Flagler<br>Beach</div>
<div class="guide" style="left:767px;top:3759px"><div class="guide-icon"><svg width="30" height="30" viewBox="0 0 30 30"><circle cx="15" cy="15" r="11" fill="none" stroke="var(--blue)" stroke-width="2.5"/><path d="M15 8 L18 15 L15 22 L12 15 Z" fill="var(--blue)"/></svg></div>Explore nearby<br>attractions</div>

<!-- FAQ -->
<div class="palm" role="img" aria-label="Palm leaf decoration" style="left:-60px;top:4110px;width:200px;height:220px"></div>
<div class="palm" role="img" aria-label="Palm leaf decoration" style="right:-40px;top:4110px;width:210px;height:240px"></div>
<p class="abs center script" style="top:4100px">Faqs</p>
<h2 class="abs center section-title" style="top:4126px">Popular Questions</h2>
<span class="underline" style="top:4171px"></span>
<div class="faq open" style="top:4208px;height:62px;padding-top:12px"><span style="color:var(--blue-mid)">Is The Condo Pet-Friendly?</span><p style="font-weight:400;font-size:10px;margin-top:8px">Yes, Our Cormant Haven Condo Welcomes Pets With Prior Approval.</p><span class="toggle" style="top:20px;margin-top:0"></span></div>
<div class="faq" style="top:4282px;height:30px;line-height:28px">How Far Is The Condo From The Beach?<span class="toggle"></span></div>
<div class="faq" style="top:4329px;height:30px;line-height:28px">Can I Book Directly On StayNest, RentHarbor, Or LeaseLocal?<span class="toggle"></span></div>
<div class="faq" style="top:4376px;height:30px;line-height:28px">Are There Family-Friendly Activities Nearby?<span class="toggle"></span></div>
<span class="btn btn-blue" style="left:560px;top:4441px;width:80px;height:30px">View All</span>

<!-- FOOTER -->
<div class="footer-band" role="img" aria-label="Ocean wave decoration"></div>
<div class="footer-body"></div>
<div class="abs" role="img" aria-label="Beach scene with palm tree, umbrella and life ring" style="left:210px;top:4500px;width:250px;height:200px;border-radius:50%;background:radial-gradient(circle at 50% 45%,#6FCCEA 0%,#f5b14a 35%,#e2452f 55%,rgba(226,69,47,0) 70%)"></div>
<div class="abs" style="left:596px;top:4668px;width:86px;height:30px;display:flex;justify-content:center"><span style="width:30px;height:30px;border-radius:50%;background:var(--cyan)"></span></div>
<p class="abs" style="left:539px;top:4716px;width:200px;text-align:center;color:var(--white);font-weight:600;font-size:16px;line-height:19px">Cormant Haven<br>Oceanfront Condo</p>

<p class="abs footer-h" style="left:156px;top:4792px">CONTACT US</p>
<div class="abs footer-list" style="left:156px;top:4815px">
  <div>✆&nbsp; 555-210-4471</div>
  <div>✆&nbsp; 555-210-4472</div>
  <div>✉&nbsp; hello@cormanthaven.com</div>
  <div style="line-height:15px;margin-top:5px;display:flex;gap:6px"><svg width="10" height="13" viewBox="0 0 10 13"><path d="M5 13 C5 13 0 7 0 5 A5 5 0 0 1 10 5 C10 7 5 13 5 13 Z" fill="var(--cyan)"/><circle cx="5" cy="5" r="2" fill="#1d2a3c"/></svg><span>742 Harbor Crest Lane,<br>Dunmore, TN 38900</span></div>
</div>

<p class="abs footer-h" style="left:382px;top:4792px">QUICK LINKS</p>
<div class="abs footer-links" style="left:382px;top:4816px">
  <div style="color:var(--cyan)">Home</div><div>Local Area</div><div>Reviews</div><div>Blogs</div><div>Faqs</div><div>Contact Us</div>
</div>

<div class="abs" role="img" aria-label="Map of the condo location along the coast" style="left:522px;top:4792px;width:232px;height:146px;border-radius:4px;background:linear-gradient(120deg,#e9efe6 0%,#dfe8dc 55%,#b9d8ea 56%,#a9cfe6 100%)"></div>

<p class="abs footer-h" style="left:793px;top:4662px">GET IN TOUCH!</p>
<div class="field" style="top:4690px;height:29px">First Name</div>
<div class="field" style="top:4734px;height:29px">Email</div>
<div class="field" style="top:4778px;height:29px">Phone</div>
<div class="field" style="top:4822px;height:64px">How Can We Help?</div>
<span class="btn btn-blue" style="left:793px;top:4902px;width:78px;height:27px;background:var(--blue-mid)">Submit</span>

<div class="bottom-bar">
  <p class="abs" style="left:156px;top:9px">© 2026 Cormant Haven Oceanfront Condo. All Right Reserved &nbsp;|&nbsp; Terms And Conditions</p>
  <span class="social" style="left:944px"></span>
  <span class="social" style="left:970px"></span>
  <span class="social" style="left:996px"></span>
  <span class="social" style="left:1022px"></span>
</div>

</body>
</html>
```